We need a fresh, new church business card!!

We need a church business card with basic info to hand out as invites. We are looking for something clean that communicates our basic information clearly.

We are open to square or rectangle card sizes.

General Public

Religious

The attached logo is the only one that I have available. We'd like to see options with with text of the logo lighter and on a dark background as well as options with white/light backgrounds.

Also, we'd like to see option with rounded corners.

• Address - 2718 Maple Row, Ashford, OH 43142
• Website - brookvane.example
• Phone - 555-555-0163
• Service times -
• Sunday - 10am Sunday School
• - 11am Family Worship
• - 6pm Night of Prayer
• Wednesday - 7:30pm Adult Bible Study
• Classes for all ages

```html
<!DOCTYPE html>
<html lang="en">
<head>
<meta charset="utf-8">
<title>Brookvane Pentecostal Church – Business Card</title>
<link rel="stylesheet" href="https://fonts.googleapis.com/css2?family=Open+Sans:wght@400;600;700&display=swap">
<style>
  :root {
    --backdrop: #5c3e2c;
    --card-light: #ffffff;
    --teal: #5792a3;
    --teal-dark: #4a8596;
    --ink: #555555;
    --ink-soft: #6b6b6b;
    --rule: #8a8a8a;
    --white: #ffffff;
  }
  * { box-sizing: border-box; margin: 0; padding: 0; }
  html, body { width: 1200px; height: 1000px; overflow: hidden; }
  body {
    background: var(--backdrop);
    font-family: "Open Sans", Arial, sans-serif;
    position: relative;
  }
  .card {
    position: absolute;
    left: 265px;
    width: 665px;
    height: 397px;
    border-radius: 28px;
    box-shadow: 0 6px 14px rgba(0,0,0,.35);
  }
  .card--front { top: 73px; background: var(--card-light); }
  .card--back { top: 532px; background: var(--teal); }

  .brand { position: absolute; display: flex; align-items: center; }
  .brand__dot { border-radius: 50%; flex: none; }
  .brand__name { font-weight: 600; display: flex; flex-direction: column; }
  .brand__main { line-height: 1; letter-spacing: .01em; }
  .brand__sub { letter-spacing: .22em; line-height: 1.2; }

  .card--front .brand { left: 32px; top: 33px; gap: 20px; }
  .card--front .brand__dot { width: 52px; height: 62px; border-radius: 50%; background: var(--teal); }
  .card--front .brand__name { color: var(--ink-soft); }
  .card--front .brand__main { font-size: 36px; }
  .card--front .brand__sub { font-size: 13px; margin-top: 4px; }

  .card--back .brand { left: 0; right: 0; top: 148px; justify-content: center; gap: 26px; }
  .card--back .brand__dot { width: 72px; height: 100px; background: var(--white); }
  .card--back .brand__name { color: var(--white); }
  .card--back .brand__main { font-size: 48px; }
  .card--back .brand__sub { font-size: 17px; margin-top: 6px; }

  .services { position: absolute; left: 32px; top: 143px; color: var(--ink); }
  .services__title { color: var(--teal-dark); font-weight: 600; font-size: 18px; line-height: 24px; }
  .services__list { list-style: none; font-size: 16.5px; line-height: 21px; }

  .person { position: absolute; right: 32px; top: 227px; text-align: right; }
  .person__name { color: var(--teal-dark); font-weight: 700; font-size: 23px; line-height: 1.2; }
  .person__role { color: var(--ink); font-size: 16px; }

  .divider { position: absolute; left: 32px; right: 32px; top: 287px; border-top: 1px solid var(--rule); }

  .contacts { position: absolute; right: 32px; top: 295px; list-style: none; text-align: right; color: var(--ink); font-size: 16px; }
  .contacts li { display: flex; justify-content: flex-end; align-items: center; gap: 8px; height: 25px; }
  .contacts svg { width: 16px; height: 16px; fill: var(--teal); }
</style>
</head>
<body>

<section class="card card--front">
  <div class="brand">
    <span class="brand__dot"></span>
    <span class="brand__name"><span class="brand__main">BROOKVANE</span><span class="brand__sub">PENTECOSTAL CHURCH</span></span>
  </div>

  <div class="services">
    <h2 class="services__title">Service times</h2>
    <ul class="services__list">
      <li>- Sunday - 10am Sunday School</li>
      <li>- 11am Family Worship</li>
      <li>- 6pm Night of Prayer</li>
      <li>- Wednesday - 7:30pm Adult Bible Study</li>
      <li>- Classes for all ages</li>
    </ul>
  </div>

  <div class="person">
    <p class="person__name">Marcus Ellery</p>
    <p class="person__role">Managing Director</p>
  </div>

  <div class="divider"></div>

  <ul class="contacts">
    <li>555-555-0163
      <svg viewBox="0 0 16 16" aria-hidden="true"><path d="M1 6c0-2 3-3 7-3s7 1 7 3v1h-3V5.5c-1-.4-2.4-.6-4-.6s-3 .2-4 .6V7H1z"/><path d="M3 8h10l1 5H2z"/></svg>
    </li>
    <li>brookvane.example
      <svg viewBox="0 0 16 16" aria-hidden="true"><path d="M8 1a7 7 0 1 0 0 14A7 7 0 0 0 8 1zm0 1.6a5.4 5.4 0 0 1 4.6 2.6H10L8.5 4 7 5.5 5 4.5 3.7 5A5.4 5.4 0 0 1 8 2.6zM3 8.5l2 1 1 2-.5 2A5.4 5.4 0 0 1 3 8.5z"/></svg>
    </li>
    <li>2718 Maple Row, Ashford, OH 43142
      <svg viewBox="0 0 16 16" aria-hidden="true"><path d="M8 1.5 0.5 8h2.2v6.5h4v-4h2.6v4h4V8h2.2z"/></svg>
    </li>
  </ul>
</section>

<section class="card card--back">
  <div class="brand">
    <span class="brand__dot"></span>
    <span class="brand__name"><span class="brand__main">BROOKVANE</span><span class="brand__sub">PENTECOSTAL CHURCH</span></span>
  </div>
</section>

</body>
</html>
```